Food label for BarBQ sauce and creole seasoning under the name HONEY BAYOU

I need a label design using the name "HONEY BAYOU" that will be used on bottles of Bar B Q sauce, both Creole and Cajun, and dry Cajun and dry Creole seasoning. I have attached a copy of the letter style we will be using. It is NOT a religious product or has any religious meaning. It comes from a saying old southerners used when they tasted something special -"Oh Honey Bayou". The labels for the Bar B Q sauces will be 5" wide by 3" tall, and the dry seasonings will be 5" wide by 3 1/2" tall. The products will that they are from South Louisiana and should reflect the typical food from the New Orleans area. This produce name is a REGISTERED TRADE NAME with the US trademark office.

```html
<!DOCTYPE html>
<html lang="en">
<head>
<meta charset="utf-8">
<title>Honey Bayou – BBQ Sauce Label</title>
<link rel="stylesheet" href="https://fonts.googleapis.com/css2?family=Titan+One&family=Rye&family=Russo+One&family=Josefin+Sans:wght@400&display=swap">
<style>
  :root {
    --page: #ffffff;
    --rim-orange: #ff6a00;
    --rim-yellow: #ffc800;
    --rim-black: #111111;
    --band: #fbfa9c;
    --title-red: #c93200;
    --name-red: #ee1c00;
    --ink: #111111;
    --white: #ffffff;
    --seasoning-edge: #ffe000;
  }
  html, body {
    margin: 0;
    padding: 0;
    width: 1200px;
    height: 972px;
    overflow: hidden;
    background: var(--page);
  }
  .label { display: block; width: 1200px; height: 972px; }
  .rim-outer { fill: var(--rim-orange); }
  .rim-mid { fill: var(--rim-yellow); }
  .rim-inner { fill: var(--rim-orange); }
  .panel { stroke: var(--rim-black); stroke-width: 7; }
  .name-band { fill: var(--band); }
  .product-title {
    font-family: "Titan One", "Arial Black", sans-serif;
    font-size: 112px;
    fill: var(--title-red);
    stroke: var(--ink);
    stroke-width: 2.5;
    paint-order: stroke;
  }
  .product-title-shadow {
    font-family: "Titan One", "Arial Black", sans-serif;
    font-size: 112px;
    fill: var(--ink);
    stroke: var(--ink);
    stroke-width: 2.5;
  }
  .brand-name {
    font-family: "Rye", Georgia, serif;
    font-size: 112px;
    fill: var(--name-red);
    stroke: var(--name-red);
    stroke-width: 1;
  }
  .flavor-shadow {
    font-family: "Russo One", "Arial Black", sans-serif;
    font-size: 72px;
    fill: var(--ink);
  }
  .flavor {
    font-family: "Russo One", "Arial Black", sans-serif;
    font-size: 72px;
    fill: var(--white);
  }
  .seasoning {
    font-family: "Josefin Sans", Arial, sans-serif;
    font-size: 40px;
    fill: var(--ink);
    stroke: var(--seasoning-edge);
    stroke-width: 3;
    paint-order: stroke;
  }
</style>
</head>
<body>
<svg class="label" viewBox="0 0 1200 972" xmlns="http://www.w3.org/2000/svg" role="img" aria-label="Honey Bayou BBQ sauce label, Cajun seasoning">
  <defs>
    <linearGradient id="panel-heat" x1="0" y1="0" x2="1" y2="0">
      <stop offset="0" stop-color="#ff8c40"/>
      <stop offset="0.15" stop-color="#ff2000"/>
      <stop offset="0.32" stop-color="#ff6000"/>
      <stop offset="0.5" stop-color="#ffcc00"/>
      <stop offset="0.68" stop-color="#ff6000"/>
      <stop offset="0.86" stop-color="#ff1000"/>
      <stop offset="1" stop-color="#ff7a00"/>
    </linearGradient>
  </defs>

  <g class="frame">
    <rect class="rim-outer" x="26" y="124" width="1146" height="692" rx="250" ry="250"/>
    <rect class="rim-mid" x="36" y="134" width="1126" height="672" rx="240" ry="240"/>
    <rect class="rim-inner" x="46" y="144" width="1106" height="652" rx="230" ry="230"/>
    <rect class="panel" x="58" y="156" width="1082" height="628" rx="220" ry="220" fill="url(#panel-heat)"/>
  </g>

  <text class="product-title-shadow" x="603" y="321" text-anchor="middle" textLength="620" lengthAdjust="spacingAndGlyphs">BBQ sauce</text>
  <text class="product-title" x="597" y="314" text-anchor="middle" textLength="620" lengthAdjust="spacingAndGlyphs">BBQ sauce</text>

  <rect class="name-band" x="73" y="361" width="1050" height="226" rx="14" ry="14"/>
  <text class="brand-name" x="598" y="515" text-anchor="middle" textLength="950" lengthAdjust="spacingAndGlyphs">HONEY BAYOU</text>

  <text class="flavor-shadow" x="604" y="697" text-anchor="middle" textLength="312" lengthAdjust="spacingAndGlyphs">CAJUN</text>
  <text class="flavor" x="599" y="691" text-anchor="middle" textLength="312" lengthAdjust="spacingAndGlyphs">CAJUN</text>
  <text class="seasoning" x="600" y="748" text-anchor="middle" textLength="268" lengthAdjust="spacingAndGlyphs">SEASONING</text>
</svg>
</body>
</html>
```